home accents e-commerce website

I'd like a professional simple website designed where I can sell my home goods. I already have my domain name registered. I need the website to accept credit card payments and Quenlo. It should have a shopping cart option and calculate sales tax and shipping costs on merchandise automatically.

I'll be taking photographs of the merchandise and writing product descriptions myself. (I'm not a professional photographer, so these photos probably won't look too polished. If you can help me make them look better, that'd be great). As I add new merchandise in the future, I'd like an option where I can log in to the back end myself and add pictures/product descriptions. And take old products down as they sell out. So the website needs to be user-friendly for me, even though I'm completely web design illiterate!

I'd like a creative, talented person who can create a whimsical, cute website. Nothing too corporate-looking.

Thank you!

Target Market(s)

women, online shoppers, New York City-area, (ship products to the United States only)

Industry/Entity Type

Home And Garden

Coding

Coded - Design and coding required

Number of Pages Required

1 page

Font styles to use
Sans Serif

Colors
0355a3
ffffff

Requirements
Must have
• shopping cart feature
• safe, secure credit card and Quenlo payments
• ability for me to go in and add new products and take down old/sold products
Nice to have
• whimsical, cute design
Should not have
• too corporate-looking

```html
<!DOCTYPE html>
<html lang="en">
<head>
<meta charset="utf-8">
<title>Hartwell Home Goods</title>
<link href="https://fonts.googleapis.com/css2?family=Jost:wght@300;400;500;600&display=swap" rel="stylesheet">
<style>
:root{
  --blue:#0355a3;
  --white:#ffffff;
  --ink:#222222;
  --text:#444444;
  --muted:#888888;
  --line:#dddddd;
  --dark:#1d1d1d;
  --nav:#111111;
  --band:#a3a3a3;
}
*{box-sizing:border-box;margin:0;padding:0}
html,body{width:1200px;height:3077px;overflow:hidden}
body{position:relative;background:var(--white);font-family:"Jost",Arial,sans-serif;color:var(--text);font-size:15px}
.abs{position:absolute}
svg{display:block}

/* header */
.topbar{top:10px;right:98px;display:flex;align-items:center;gap:22px;font-size:14px;color:var(--ink)}
.topbar span{display:flex;align-items:center;gap:7px}
.social{display:flex;gap:7px}
.social i{width:27px;height:27px;background:var(--nav);display:flex;align-items:center;justify-content:center}
.social i::after{content:"";width:9px;height:9px;border-radius:50%;background:var(--white)}
.logo-block{top:30px;left:98px;width:224px;height:98px;display:flex;flex-direction:column;align-items:center;justify-content:center}
.logo-name{font-size:54px;font-weight:600;color:var(--blue);line-height:1;letter-spacing:1px}
.logo-sub{font-size:17px;letter-spacing:7px;color:var(--blue);margin-top:4px}
.header-tools{top:73px;right:98px;display:flex;gap:6px;align-items:center}
.tool{height:30px;min-width:36px;background:var(--nav);color:var(--white);display:flex;align-items:center;justify-content:center;gap:4px;font-size:12px;padding:0 6px}
.cart-total{border:1px solid var(--line);height:30px;display:flex;align-items:center;padding:0 10px 0 0;font-size:12px;color:var(--ink);gap:8px}
.cart-total b{background:var(--blue);width:30px;height:30px;display:flex;align-items:center;justify-content:center}

.mainnav{top:135px;left:0;width:1200px;height:54px;background:var(--nav)}
.mainnav ul{position:absolute;left:98px;top:0;display:flex;list-style:none;height:54px}
.mainnav li{color:var(--white);font-size:13.5px;white-space:nowrap;display:flex;align-items:center;justify-content:center;border-right:1px solid #333;text-transform:uppercase}
.mainnav li.home{width:101px;background:var(--blue)}
.mainnav li.about{width:157px}
.mainnav li.how{width:283px}
.mainnav li.contact{width:141px;border-right:none}
.search{position:absolute;left:782px;top:8px;width:265px;height:38px;background:#333;color:#999;font-size:13px;display:flex;align-items:center;padding-left:14px}
.search-btn{position:absolute;left:1049px;top:0;width:52px;height:54px;background:var(--blue);display:flex;align-items:center;justify-content:center}

/* sidebar */
.cats{top:221px;left:98px;width:259px;height:431px;border:1px solid var(--line)}
.cats h3{height:52px;background:#2a2a2a;color:var(--white);font-size:17px;font-weight:500;display:flex;align-items:center;gap:12px;padding-left:16px}
.cats ul{list-style:none;padding:8px 28px 0 22px}
.cats li{height:38px;border-bottom:1px solid #eee;display:flex;align-items:center;font-size:15px;color:var(--text)}
.cats li:last-child{border:none}
.cats li::before{content:"›";color:#aaa;margin-right:14px}

/* hero */
.hero{top:221px;left:388px;width:713px;height:431px;background:linear-gradient(90deg,#cfc8bf 0%,#e5ddd4 40%,#ece7e2 70%,#e7e3df 100%)}
.hero-copy{position:absolute;left:458px;top:80px;color:var(--blue);font-size:48px;line-height:1.1;font-weight:400}
.badge{position:absolute;left:592px;top:102px;width:68px;height:68px;border-radius:50%;background:var(--blue);color:var(--white);font-size:20px;line-height:1;display:flex;flex-direction:column;align-items:center;justify-content:center;font-weight:500}
.badge small{font-size:18px}
.shop-btn{position:absolute;left:458px;top:254px;width:194px;height:46px;background:var(--blue);color:var(--white);font-size:19px;display:flex;align-items:center;justify-content:center;gap:6px}
.dots{position:absolute;right:26px;bottom:18px;display:flex;gap:6px}
.dots i{width:9px;height:9px;border-radius:50%;background:rgba(255,255,255,.6)}
.dots i:first-child{background:var(--white)}

.tile{top:687px;width:318px;height:211px;display:flex;align-items:center;justify-content:center}
.tile span{width:100%;background:rgba(40,40,40,.45);color:var(--white);font-size:26px;text-align:center;padding:6px 0;text-transform:uppercase}

.wave{left:98px;width:1003px;height:10px}

.sec-title{left:0;width:1200px;text-align:center;font-size:33px;color:var(--ink);font-weight:400}
.sec-title b{color:var(--blue);font-weight:400}
.sec-title::before,.sec-title::after{content:"";display:inline-block;width:140px;height:1px;background:var(--line);vertical-align:middle;margin:0 22px}

.tabs{top:1081px;left:370px;display:flex;align-items:center;font-size:17px;color:var(--text)}
.tabs span{padding:0 32px;border-right:1px solid var(--line)}
.tabs span:last-child{border:none}
.tabs span.on{border:1px solid var(--line);padding:7px 30px;margin-right:0}

.card{width:232px;height:363px;border:1px solid var(--line);background:var(--white);overflow:hidden}
.card.on{border-color:var(--blue)}
.card .ph{height:225px}
.stars{margin:24px auto 0;width:130px;display:flex;align-items:center;gap:6px;justify-content:center}
.stars::before,.stars::after{content:"";flex:1;height:1px;background:var(--line)}
.stars span{font-size:13px;color:var(--blue);letter-spacing:1px}
.stars span em{color:#bbb;font-style:normal}
.pname{text-align:center;font-size:16px;color:var(--ink);margin-top:12px}
.price{text-align:center;font-size:18px;margin-top:20px}
.price s{color:var(--muted);margin-right:14px}
.price b{color:var(--blue);font-weight:400}
.ribbon{position:absolute;right:0;top:0;width:60px;height:60px}
.actions{top:1914px;left:98px;width:232px;height:41px;display:flex}
.actions i{flex:1;background:#8a8a8a;display:flex;align-items:center;justify-content:center;border-right:1px solid #a0a0a0}
.actions i:last-child{background:var(--blue);border:none}

.viewall{top:1959px;left:503px;width:194px;height:45px;background:var(--nav);color:var(--white);font-size:19px;display:flex;align-items:center;justify-content:center;gap:6px}

.deal{top:2193px;width:488px;height:221px;border:1px solid var(--line);display:flex;padding:6px}
.deal .ph{width:240px;height:207px}
.deal .info{flex:1;text-align:center;padding-top:16px}
.deal .info .stars{margin-top:8px}
.deal .pname{margin-top:10px}
.deal .price{margin-top:18px}
.deal p{font-size:13px;line-height:1.6;color:var(--text);margin:14px 18px 0}

.band{top:2467px;left:0;width:1200px;height:160px;background:var(--band)}
.perk{top:2521px;width:232px;height:55px;background:var(--white);border:1px solid var(--line);display:flex;align-items:center;gap:14px;padding-left:18px;font-size:13px;color:var(--ink);line-height:1.3}
.perk.first{color:var(--blue);border-bottom:3px solid var(--blue)}

.footer{top:2627px;left:0;width:1200px;height:398px;background:var(--dark);color:#ccc}
.f-logo{position:absolute;left:98px;top:56px;color:#ddd}
.f-logo .logo-name{color:#ddd;font-size:46px}
.f-logo .logo-sub{color:#ddd;font-size:15px;letter-spacing:8px}
.f-about{position:absolute;left:98px;top:150px;width:320px;font-size:12.5px;line-height:1.7;color:#ccc}
.f-col{position:absolute;top:100px;font-size:13px}
.f-col h4{color:var(--white);font-weight:500;font-size:14px;margin-bottom:18px;text-transform:uppercase}
.f-col li{list-style:none;margin-bottom:9px;color:#bbb}
.f-col li::before{content:"›";margin-right:8px}
.f-contact div{display:flex;gap:10px;margin-bottom:12px;color:#ccc;line-height:1.5}
.f-rule{position:absolute;left:98px;top:285px;width:1003px;height:1px;background:#333}
.news{position:absolute;left:98px;top:310px;display:flex;align-items:center;gap:14px;color:var(--white);font-size:23px}
.news-ico{width:40px;height:38px;background:var(--blue);display:flex;align-items:center;justify-content:center}
.news-input{position:absolute;left:380px;top:316px;width:318px;height:38px;background:var(--white);color:#999;font-size:13px;display:flex;align-items:center;padding-left:12px}
.news-btn{position:absolute;left:706px;top:316px;width:120px;height:38px;background:var(--blue);color:var(--white);font-size:15px;display:flex;align-items:center;justify-content:center}
.f-social{position:absolute;right:98px;top:317px;display:flex;gap:8px}
.f-social i{width:36px;height:36px;border:1px solid #555;background:#111;display:flex;align-items:center;justify-content:center}
.f-social i::after{content:"";width:11px;height:11px;border-radius:50%;background:var(--white)}

.copy{top:3042px;left:98px;font-size:14px;color:var(--ink)}
.pay{top:3036px;right:98px;display:flex;gap:16px;font-size:15px;font-weight:500;color:var(--blue)}
</style>
</head>
<body>

<!-- header -->
<div class="abs topbar">
  <span><svg width="14" height="14" viewBox="0 0 24 24"><path d="M6.6 10.8a15 15 0 0 0 6.6 6.6l2.2-2.2c.3-.3.7-.4 1-.2 1.1.4 2.3.6 3.6.6.6 0 1 .4 1 1V20c0 .6-.4 1-1 1A17 17 0 0 1 3 4c0-.6.4-1 1-1h3.5c.6 0 1 .4 1 1 0 1.3.2 2.5.6 3.6.1.3 0 .7-.2 1z" fill="#111"/></svg>+1 212 555.0148</span>
  <span><svg width="15" height="12" viewBox="0 0 24 18"><rect x="1" y="1" width="22" height="16" fill="none" stroke="#111" stroke-width="2"/><path d="M1 1l11 9 11-9" fill="none" stroke="#111" stroke-width="2"/></svg>hello@hartwellhome.com</span>
  <div class="social"><i></i><i></i><i></i><i></i></div>
</div>

<div class="abs logo-block">
  <div class="logo-name">hartwell</div>
  <div class="logo-sub">HOME GOODS</div>
</div>

<div class="abs header-tools">
  <div class="tool"><svg width="14" height="14" viewBox="0 0 24 24"><rect x="5" y="10" width="14" height="11" fill="none" stroke="#fff" stroke-width="2"/><path d="M8 10V7a4 4 0 0 1 8 0v3" fill="none" stroke="#fff" stroke-width="2"/></svg></div>
  <div class="tool"><svg width="14" height="13" viewBox="0 0 24 22"><path d="M12 21 3 12a5 5 0 0 1 9-6 5 5 0 0 1 9 6z" fill="none" stroke="#fff" stroke-width="2"/></svg>0</div>
  <div class="tool"><svg width="14" height="14" viewBox="0 0 24 24"><path d="M4 12a8 8 0 0 1 14-5M20 12a8 8 0 0 1-14 5" fill="none" stroke="#fff" stroke-width="2"/><path d="M18 3v4h-4M6 21v-4h4" fill="none" stroke="#fff" stroke-width="2"/></svg>0</div>
  <div class="cart-total"><b><svg width="16" height="14" viewBox="0 0 24 22"><path d="M1 2h4l3 12h12l3-9H7" fill="none" stroke="#fff" stroke-width="2"/><circle cx="9" cy="19" r="2" fill="#fff"/><circle cx="19" cy="19" r="2" fill="#fff"/></svg></b>(0)items - $0.00</div>
</div>

<nav class="abs mainnav">
  <ul>
    <li class="home">Home</li>
    <li class="about">About Hartwell</li>
    <li class="how">How does this craziness work?</li>
    <li class="contact">Contact Us</li>
  </ul>
  <div class="search">Type Keyword...</div>
  <div class="search-btn"><svg width="18" height="18" viewBox="0 0 24 24"><circle cx="10" cy="10" r="7" fill="none" stroke="#fff" stroke-width="2.5"/><path d="M15 15l7 7" stroke="#fff" stroke-width="2.5"/></svg></div>
</nav>

<!-- categories -->
<aside class="abs cats">
  <h3><svg width="20" height="14" viewBox="0 0 20 14"><path d="M0 1h20M0 7h20M0 13h20" stroke="#fff" stroke-width="2"/></svg>SHOP BY CATEGORIES</h3>
  <ul>
    <li>Vases</li>
    <li>Throw Pillows</li>
    <li>Blankets and Throws</li>
    <li>For Your Floors</li>
    <li>For Your Walls</li>
    <li>For Your Table</li>
    <li>For Your Bedside</li>
    <li>Let THere Be Light</li>
    <li>Put Your Feet Up</li>
  </ul>
</aside>

<!-- hero -->
<section class="abs hero">
  <div class="abs" role="img" aria-label="Photo of colourful throw pillows, a fringed blanket and a vase of purple flowers on a wooden floor" style="left:0;top:0;width:440px;height:431px;background:linear-gradient(135deg,#bdb3a8 0%,#c9846a 35%,#8a3e6e 55%,#c94f7a 70%,#d8c3a8 100%);opacity:.75"></div>
  <div class="hero-copy">NEW<br>LOOK<br>VASES</div>
  <div class="badge">20%<small>OFF</small></div>
  <div class="shop-btn">SHOP NOW <span>»</span></div>
  <div class="dots"><i></i><i></i><i></i><i></i></div>
</section>

<div class="abs tile" role="img" aria-label="Living room with vases and cushions" style="left:98px;background:linear-gradient(135deg,#d9d9d6,#8c9298 60%,#4c5258)"><span>Vases</span></div>
<div class="abs tile" role="img" aria-label="Window seat with throw pillows" style="left:441px;background:linear-gradient(135deg,#e6e3de,#c9a88a 50%,#a33c2c)"><span>Throw Pillows</span></div>
<div class="abs tile" role="img" aria-label="Bedroom with blankets and throws" style="left:783px;background:linear-gradient(135deg,#c7c4be,#8f8b86 60%,#5b5955)"><span>Blankets and Throws</span></div>

<svg class="abs wave" style="top:951px" viewBox="0 0 1003 10" preserveAspectRatio="none"><path d="M0 5 Q5 0 10 5 T20 5 T30 5 T40 5 T50 5 T60 5 T70 5 T80 5 T90 5 T100 5 T110 5 T120 5 T130 5 T140 5 T150 5 T160 5 T170 5 T180 5 T190 5 T200 5 T210 5 T220 5 T230 5 T240 5 T250 5 T260 5 T270 5 T280 5 T290 5 T300 5 T310 5 T320 5 T330 5 T340 5 T350 5 T360 5 T370 5 T380 5 T390 5 T400 5 T410 5 T420 5 T430 5 T440 5 T450 5 T460 5 T470 5 T480 5 T490 5 T500 5 T510 5 T520 5 T530 5 T540 5 T550 5 T560 5 T570 5 T580 5 T590 5 T600 5 T610 5 T620 5 T630 5 T640 5 T650 5 T660 5 T670 5 T680 5 T690 5 T700 5 T710 5 T720 5 T730 5 T740 5 T750 5 T760 5 T770 5 T780 5 T790 5 T800 5 T810 5 T820 5 T830 5 T840 5 T850 5 T860 5 T870 5 T880 5 T890 5 T900 5 T910 5 T920 5 T930 5 T940 5 T950 5 T960 5 T970 5 T980 5 T990 5 T1003 5" fill="none" stroke="#cccccc" stroke-width="1.5"/></svg>

<!-- featured -->
<h2 class="abs sec-title" style="top:1005px">Featured <b>Products</b></h2>
<div class="abs tabs"><span class="on">Latest</span><span>Best Seller</span><span>Special</span><span>New Arrival</span></div>

<div class="abs card" style="left:98px;top:1161px"><div class="ph" role="img" aria-label="White patterned vases with yellow flowers" style="background:linear-gradient(180deg,#f4f4f2,#e8e6e0)"></div><div class="stars"><span>★★★<em>☆☆</em></span></div><div class="pname">Product Name 1</div><div class="price"><s>$156.00</s><b>$156.00</b></div></div>
<div class="abs card" style="left:355px;top:1161px"><div class="ph" role="img" aria-label="Pile of bright coloured pillows" style="background:linear-gradient(135deg,#c9c2c6,#b2265b 35%,#e26a2c 60%,#5d2a1a)"></div><svg class="ribbon" viewBox="0 0 60 60"><path d="M0 0h60v60z" fill="#0355a3"/><text x="42" y="24" fill="#fff" font-family="Jost,sans-serif" font-size="13" transform="rotate(45 42 24)" text-anchor="middle">New</text></svg><div class="stars"><span>★★★<em>☆☆</em></span></div><div class="pname">Product Name 2</div><div class="price"><s>$156.00</s><b>$156.00</b></div></div>
<div class="abs card" style="left:611px;top:1161px"><div class="ph" role="img" aria-label="Armchair with a cream throw" style="background:linear-gradient(180deg,#e8d9a8,#c9a766 60%,#8a5a2c)"></div><div class="stars"><span>★★★<em>☆☆</em></span></div><div class="pname">Product Name 3</div><div class="price"><s>$156.00</s><b>$156.00</b></div></div>
<div class="abs card" style="left:869px;top:1161px"><div class="ph" role="img" aria-label="Table lamp on a side table" style="background:linear-gradient(180deg,#eceae6,#c9b9a2 60%,#4a3a2c)"></div><div class="stars"><span>★★★<em>☆☆</em></span></div><div class="pname">Product Name 4</div><div class="price"><s>$156.00</s><b>$156.00</b></div></div>

<div class="abs card on" style="left:98px;top:1551px"><div class="ph" role="img" aria-label="Candle holders on a patterned table runner" style="background:linear-gradient(180deg,#d8d2c6,#b8a890 60%,#8d7a60)"></div><div class="stars"><span>★★★<em>☆☆</em></span></div><div class="pname">Product Name 1</div><div class="price"><s>$156.00</s><b>$156.00</b></div></div>
<div class="abs card" style="left:355px;top:1551px"><div class="ph" role="img" aria-label="Living room with fireplace and wood floor" style="background:linear-gradient(180deg,#3d2c20,#7a5530 55%,#c99a5e)"></div><div class="stars"><span>★★★<em>☆☆</em></span></div><div class="pname">Product Name 2</div><div class="price"><s>$156.00</s><b>$156.00</b></div></div>
<div class="abs card" style="left:611px;top:1551px"><div class="ph" role="img" aria-label="Carved stone vase with leaves" style="background:linear-gradient(180deg,#f2f2f0,#bdb6ac 60%,#9a938a)"></div><svg class="ribbon" viewBox="0 0 60 60"><path d="M0 0h60v60z" fill="#0355a3"/><text x="42" y="24" fill="#fff" font-family="Jost,sans-serif" font-size="13" transform="rotate(45 42 24)" text-anchor="middle">Sell</text></svg><div class="stars"><span>★★★<em>☆☆</em></span></div><div class="pname">Product Name 3</div><div class="price"><s>$156.00</s><b>$156.00</b></div></div>
<div class="abs card" style="left:869px;top:1551px"><div class="ph" role="img" aria-label="Dark wood coffee table on a rug" style="background:linear-gradient(180deg,#e6e2d8,#3a2e26 55%,#b8aa98)"></div><div class="stars"><span>★★★<em>☆☆</em></span></div><div class="pname">Product Name 4</div><div class="price"><s>$156.00</s><b>$156.00</b></div></div>

<div class="abs actions">
  <i><svg width="14" height="13" viewBox="0 0 24 22"><path d="M12 21 3 12a5 5 0 0 1 9-6 5 5 0 0 1 9 6z" fill="#fff"/></svg></i>
  <i><svg width="15" height="13" viewBox="0 0 24 22"><path d="M1 2h4l3 12h12l3-9H7" fill="none" stroke="#fff" stroke-width="2.5"/><circle cx="9" cy="19" r="2" fill="#fff"/><circle cx="19" cy="19" r="2" fill="#fff"/></svg></i>
  <i><svg width="13" height="13" viewBox="0 0 24 24"><path d="M3 3l7 7M21 3l-7 7M3 21l7-7M21 21l-7-7M3 3h5M3 3v5M21 3h-5M21 3v5M3 21h5M3 21v-5M21 21h-5M21 21v-5" stroke="#fff" stroke-width="2.5" fill="none"/></svg></i>
  <i><svg width="14" height="14" viewBox="0 0 24 24"><circle cx="10" cy="10" r="7" fill="none" stroke="#fff" stroke-width="3"/><path d="M15 15l7 7" stroke="#fff" stroke-width="3"/></svg></i>
</div>

<div class="abs viewall">VIEW ALL <span>»</span></div>

<svg class="abs wave" style="top:2054px" viewBox="0 0 1003 10" preserveAspectRatio="none"><path d="M0 5 Q5 0 10 5 T20 5 T30 5 T40 5 T50 5 T60 5 T70 5 T80 5 T90 5 T100 5 T110 5 T120 5 T130 5 T140 5 T150 5 T160 5 T170 5 T180 5 T190 5 T200 5 T210 5 T220 5 T230 5 T240 5 T250 5 T260 5 T270 5 T280 5 T290 5 T300 5 T310 5 T320 5 T330 5 T340 5 T350 5 T360 5 T370 5 T380 5 T390 5 T400 5 T410 5 T420 5 T430 5 T440 5 T450 5 T460 5 T470 5 T480 5 T490 5 T500 5 T510 5 T520 5 T530 5 T540 5 T550 5 T560 5 T570 5 T580 5 T590 5 T600 5 T610 5 T620 5 T630 5 T640 5 T650 5 T660 5 T670 5 T680 5 T690 5 T700 5 T710 5 T720 5 T730 5 T740 5 T750 5 T760 5 T770 5 T780 5 T790 5 T800 5 T810 5 T820 5 T830 5 T840 5 T850 5 T860 5 T870 5 T880 5 T890 5 T900 5 T910 5 T920 5 T930 5 T940 5 T950 5 T960 5 T970 5 T980 5 T990 5 T1003 5" fill="none" stroke="#cccccc" stroke-width="1.5"/></svg>

<!-- hot deals -->
<h2 class="abs sec-title" style="top:2108px">Hot <b>Deals</b></h2>

<div class="abs deal" style="left:98px">
  <div class="ph" role="img" aria-label="Pink peonies in glass vases" style="background:linear-gradient(135deg,#f1f1f0,#e9b7c8 50%,#d9dcd8)"></div>
  <div class="info"><div class="stars"><span>★★★<em>☆☆</em></span></div><div class="pname">Product Name 1</div><div class="price"><s>$156.00</s><b>$156.00</b></div><p>Duis autem vel eum iriure dolom in hendrerit in vulputate velit essel molestie facilisi.</p></div>
</div>
<div class="abs deal" style="left:613px">
  <div class="ph" role="img" aria-label="Bench with patterned cushions" style="background:linear-gradient(135deg,#d8d2c2,#c9b27a 45%,#4a4a52 75%,#e8e6e2)"></div>
  <div class="info"><div class="stars"><span>★★★<em>☆☆</em></span></div><div class="pname">Product Name 2</div><div class="price"><s>$156.00</s><b>$156.00</b></div><p>Duis autem vel eum iriure dolom in hendrerit in vulputate velit essel molestie facilisi.</p></div>
</div>

<!-- service band -->
<div class="abs band"></div>
<div class="abs perk first" style="left:98px"><svg width="26" height="18" viewBox="0 0 26 18"><rect x="0" y="2" width="15" height="11" fill="#0355a3"/><path d="M15 5h6l4 4v4h-10z" fill="#0355a3"/><circle cx="5" cy="15" r="2.5" fill="#0355a3"/><circle cx="20" cy="15" r="2.5" fill="#0355a3"/></svg><span>FREE SHIPPING On Order<br>Over $99</span></div>
<div class="abs perk" style="left:355px"><svg width="22" height="22" viewBox="0 0 24 24"><circle cx="12" cy="12" r="10" fill="none" stroke="#222" stroke-width="2"/><circle cx="12" cy="12" r="4" fill="none" stroke="#222" stroke-width="2"/><path d="M5 5l4 4M19 5l-4 4M5 19l4-4M19 19l-4-4" stroke="#222" stroke-width="2"/></svg><span>Need Help<br>+1 212 555.0148</span></div>
<div class="abs perk" style="left:611px"><svg width="26" height="16" viewBox="0 0 26 16"><rect x="1" y="1" width="24" height="14" fill="none" stroke="#222" stroke-width="2"/><circle cx="13" cy="8" r="3.5" fill="none" stroke="#222" stroke-width="2"/></svg><span>Money Back Guarantee</span></div>
<div class="abs perk" style="left:869px"><svg width="24" height="20" viewBox="0 0 24 20"><rect x="1" y="5" width="22" height="14" fill="#222"/><rect x="8" y="1" width="8" height="5" fill="none" stroke="#222" stroke-width="2"/></svg><span>30 Days Return Service</span></div>

<!-- footer -->
<footer class="abs footer">
  <div class="f-logo"><div class="logo-name">hartwell</div><div class="logo-sub">HOME GOODS</div></div>
  <p class="f-about">Ut wisi enim ad minim veniam, quis nostrud exercim ori tation ullamcorper suscipit lobortis nisl ut aliquip ex eal commodo consequat. Duis autem vel eum ok iriure dolorn in hendrerit in vulputate velit essel molestie consequati.</p>
  <div class="f-col" style="left:509px"><h4>My Account</h4><ul><li>My Orders</li><li>My Credit Slips</li><li>My Addresses</li><li>My Personal Info</li></ul></div>
  <div class="f-col" style="left:710px"><h4>Information</h4><ul><li>Specials</li><li>New Products</li><li>Best Sellers</li><li>Our Stores</li><li>Contact Us</li></ul></div>
  <div class="f-col f-contact" style="left:905px"><h4>Information</h4>
    <div><svg width="12" height="16" viewBox="0 0 12 16" style="margin-top:3px"><path d="M6 0a6 6 0 0 1 6 6c0 4-6 10-6 10S0 10 0 6a6 6 0 0 1 6-6z" fill="#ccc"/><circle cx="6" cy="6" r="2" fill="#1d1d1d"/></svg><span>Hartwell Home Goods<br>48 Linden Row,<br>Brookvale, NY 10221</span></div>
    <div style="padding-left:22px">+1 212 555.0148</div>
    <div style="margin-top:14px"><svg width="14" height="11" viewBox="0 0 24 18" style="margin-top:4px"><rect x="0" y="0" width="24" height="18" fill="#ccc"/><path d="M0 0l12 10 12-10" fill="none" stroke="#1d1d1d" stroke-width="2"/></svg><span>hello@hartwellhome.com</span></div>
  </div>
  <div class="f-rule"></div>
  <div class="news"><div class="news-ico"><svg width="20" height="15" viewBox="0 0 24 18"><rect x="1" y="1" width="22" height="16" fill="none" stroke="#fff" stroke-width="2"/><path d="M1 1l11 9 11-9" fill="none" stroke="#fff" stroke-width="2"/></svg></div>Newsletter Signup</div>
  <div class="news-input">Your e-mail</div>
  <div class="news-btn">SIGNUP</div>
  <div class="f-social"><i></i><i></i><i></i><i></i></div>
</footer>

<div class="abs copy">Copyright © 2017 Hartwell Home Goods. All Right Reserved.</div>
<div class="abs pay"><span>Cardora</span><span>Vexa</span><span>Quenlo</span><span>Mondo</span></div>

</body>
</html>
```